I need to redesign this website. Modern Fun Professional Redesign For www.JollyPerkHub.com = New Name www.ClaimVouchly.com

Use existing content as it is on website exactly and we will revise after initial mock ups.

The new name will be ClaimVouchly.com please make a quick logo for this site too while redesigning.

Make it look like an official website....

Target Market(s)

Consumers that are redeeming certificates that businesses gave to them as a gift for customer loyalty,e tc.

Industry/Entity Type

It Professional

Logo Text

www.ClaimVouchly.com

Number of Pages Required

4 page

Colors

Designer to choose colors to be used in the design.

Requirements
Must have
• Must look professional, build trust and credibility.
Nice to have
• open
Should not have
• open

```html
<!DOCTYPE html>
<html lang="en">
<head>
<meta charset="UTF-8">
<title>ClaimVouchly.com – The Redemption Source</title>
<link href="https://fonts.googleapis.com/css2?family=Lato:ital,wght@0,400;0,700;0,900;1,400;1,700&display=swap" rel="stylesheet">
<style>
:root{
  --purple:#6a2a8e;
  --purple-dark:#4e1c6b;
  --red:#d8262e;
  --ink:#2c2c2c;
  --muted:#666;
  --sand:#e9dcc4;
  --sky:#bfe6f3;
  --white:#fff;
}
*{box-sizing:border-box;margin:0;padding:0}
html,body{width:831px;height:1200px;overflow:hidden;background:var(--white)}
body{font-family:"Lato",Arial,sans-serif;color:var(--ink);position:relative}
.page{position:relative;width:831px;height:1200px;overflow:hidden}

/* header */
.site-header{position:absolute;top:0;left:0;width:831px;height:58px;background:var(--white);z-index:3}
.brand{position:absolute;left:22px;top:12px;display:flex;align-items:center;gap:8px}
.brand-mark{width:30px;height:30px;background:var(--purple);border-radius:4px}
.brand-name{font-size:24px;font-weight:900;color:var(--purple)}
.phone{position:absolute;right:22px;top:8px;font-size:15px;color:var(--purple);font-weight:700;display:flex;align-items:center;gap:6px}
.main-nav{position:absolute;right:22px;top:34px;display:flex;gap:30px;font-size:13px}
.main-nav a{color:var(--ink);text-decoration:none}
.main-nav a.active{color:var(--purple);font-weight:700}
.nav-rule{position:absolute;left:440px;right:22px;top:54px;height:1px;background:var(--purple)}

/* hero */
.hero{position:absolute;top:58px;left:0;width:831px;height:300px}
.hero-scene{position:absolute;inset:0;background:linear-gradient(180deg,#f3ede2 0%,#ece2cf 55%,#d9c29b 100%)}
.hero-content{position:absolute;inset:0;text-align:center;padding-top:48px}
.hero h1{font-size:27px;font-weight:700;line-height:1.15;color:#3a3a3a}
.hero .subtitle{font-size:15px;margin-top:8px;color:#4a4a4a}
.hero .intro{font-size:15px;font-weight:700;color:var(--purple);line-height:1.35;margin-top:8px}
.redeem-form{display:flex;justify-content:center;margin-top:14px;gap:8px}
.redeem-form .field{width:220px;height:34px;background:var(--white);border:1px solid #ccc;font-size:12px;font-style:italic;color:var(--red);text-align:left;padding:9px 10px}
.redeem-form .go{width:46px;height:34px;background:var(--purple);color:var(--white);font-weight:700;font-size:16px;border-radius:3px;display:flex;align-items:center;justify-content:center}

/* about */
.about{position:absolute;top:392px;left:0;width:831px;text-align:center;font-size:15px;line-height:1.55}
.about p{margin-bottom:10px}
.about .motto{font-weight:700;font-style:italic}
.about .help{color:var(--purple);text-decoration:underline;font-weight:700}
.rule{position:absolute;top:600px;left:110px;width:611px;height:1px;background:#ddd}

/* reviews */
.reviews{position:absolute;top:625px;left:0;width:831px;text-align:center}
.reviews h2{font-size:23px;font-style:italic;font-weight:700;color:#333}
.avatar{width:56px;height:56px;border-radius:50%;background:#c9c3bd;margin:14px auto 10px;border:3px solid #eee}
.quote{font-size:11.5px;color:var(--muted);width:520px;margin:0 auto;line-height:1.5}
.reviewer{font-size:11px;margin-top:8px;color:#444}
.review-date{font-size:11px;color:var(--purple)}
.dots{display:flex;justify-content:center;gap:6px;margin-top:16px}
.dots span{width:16px;height:3px;background:#ccc}
.dots span.on{background:var(--red)}
.more{display:inline-block;margin-top:16px;font-size:12px;color:var(--purple);text-decoration:underline}

/* steps */
.steps{position:absolute;top:912px;left:0;width:831px;height:162px;background:linear-gradient(180deg,#d8f0f8,var(--sky))}
.steps-title{position:absolute;left:20px;top:16px;font-size:21px;font-weight:900;color:var(--red);line-height:1.15}
.steps-title span{color:var(--purple)}
.plane{position:absolute;left:18px;top:86px;width:290px;height:62px;border-radius:30px;background:linear-gradient(90deg,#ffffff,#ece6f2)}
.step{position:absolute;top:14px;width:88px;height:138px;background:var(--white);border-radius:4px;overflow:hidden;box-shadow:0 2px 6px rgba(0,0,0,.15);text-align:center}
.step-head{background:var(--red);color:var(--white);padding:5px 4px 6px}
.step-num{font-size:26px;font-weight:900;line-height:1}
.step-text{font-size:9px;line-height:1.25;margin-top:3px}
.step-icon{width:30px;height:30px;border-radius:50%;border:2px solid var(--red);margin:10px auto 0;display:flex;align-items:center;justify-content:center}
.step-btn{display:inline-block;margin-top:8px;background:var(--purple);color:var(--white);font-size:9px;padding:4px 8px;border-radius:2px}
.done{position:absolute;left:728px;top:46px;width:90px;height:46px;border-radius:24px;background:var(--white);color:var(--red);font-weight:900;font-size:21px;display:flex;align-items:center;justify-content:center}

/* footer */
.site-footer{position:absolute;top:1074px;left:0;width:831px;height:126px;background:var(--purple)}
.foot-nav{position:absolute;left:22px;top:24px;display:flex;gap:30px;font-size:13px}
.foot-nav a{color:var(--white);text-decoration:none}
.follow{position:absolute;left:360px;top:22px;color:var(--white);font-size:13px}
.socials{display:flex;gap:8px;margin-top:8px}
.socials span{width:24px;height:24px;border-radius:50%;background:var(--white)}
.copyright{position:absolute;left:22px;bottom:16px;color:#e6d8ef;font-size:11px}
.foot-brand{position:absolute;right:22px;bottom:22px;display:flex;align-items:center;gap:8px}
.foot-brand .brand-mark{background:var(--white)}
.foot-brand .brand-name{color:var(--white)}
</style>
</head>
<body>
<div class="page">

  <header class="site-header">
    <div class="brand"><span class="brand-mark"></span><span class="brand-name">ClaimVouchly</span></div>
    <div class="phone">
      <svg width="14" height="14" viewBox="0 0 24 24"><path fill="#d8262e" d="M6.6 10.8a15 15 0 0 0 6.6 6.6l2.2-2.2a1 1 0 0 1 1-.25 11.4 11.4 0 0 0 3.6.57 1 1 0 0 1 1 1V20a1 1 0 0 1-1 1A17 17 0 0 1 3 4a1 1 0 0 1 1-1h3.5a1 1 0 0 1 1 1c0 1.25.2 2.45.57 3.57a1 1 0 0 1-.25 1z"/></svg>
      123-456-7890
    </div>
    <nav class="main-nav">
      <a class="active" href="#">Home</a><a href="#">Contact Us</a><a href="#">Testimonials</a><a href="#">Terms</a>
    </nav>
    <div class="nav-rule"></div>
  </header>

  <section class="hero">
    <div class="hero-scene" role="img" aria-label="Sunny beach with palm trees, sand and a parked vintage car"></div>
    <div class="hero-content">
      <h1>Welcome To<br>The Redemption Source</h1>
      <p class="subtitle">Redemption Process Center</p>
      <p class="intro">Please Enter A Valid Certificate Id In The Form Below<br>To Redeem Your Certificate And To View Faq's, Terms And Locations.</p>
      <div class="redeem-form"><div class="field">Certificate Id</div><div class="go">Go</div></div>
    </div>
  </section>

  <section class="about">
    <p>ClaimVouchly.com is a leading company in travel certificate fulfillment.</p>
    <p>Our goal is to make it easy for you to redeem your certificate and our philosophy is this:<br><span class="motto">"What good is it to receive a gift certificate if you can't use it?"</span></p>
    <p>If you have any questions about how to redeem a certain certificate, please contact us.</p>
    <p><a class="help" href="#">We are here to help.</a></p>
  </section>
  <div class="rule"></div>

  <section class="reviews">
    <h2>Happy Customer Reviews</h2>
    <div class="avatar" role="img" aria-label="Customer portrait"></div>
    <p class="quote">Nadia was a "saving grace" She followed up and helped me book the vacation and air fare. Nadia was positive and did everything she promised to do.</p>
    <p class="reviewer">Lena T. - Wilton, GA</p>
    <p class="review-date">Added on 06/23/2017 04:24:11 pm</p>
    <div class="dots"><span></span><span class="on"></span><span></span></div>
    <a class="more" href="#">Click here to view more testimonials</a>
  </section>

  <section class="steps">
    <div class="steps-title">Ready for redemption?<br><span>Here are the 4 easy steps!</span></div>
    <div class="plane" role="img" aria-label="Passenger airplane flying among clouds"></div>

    <div class="step" style="left:327px">
      <div class="step-head"><div class="step-num">01</div><div class="step-text">Click the Redeem Now button below</div></div>
      <span class="step-btn">Redeem Now</span>
    </div>
    <div class="step" style="left:430px">
      <div class="step-head"><div class="step-num">02</div><div class="step-text">Send your form and pay the fee</div></div>
      <div class="step-icon"><svg width="16" height="16" viewBox="0 0 24 24"><path fill="none" stroke="#d8262e" stroke-width="2" d="M3 6h18v12H3zM3 6l9 7 9-7"/></svg></div>
    </div>
    <div class="step" style="left:532px">
      <div class="step-head"><div class="step-num">03</div><div class="step-text">Receive your travel voucher by email</div></div>
      <div class="step-icon"><svg width="16" height="16" viewBox="0 0 24 24"><path fill="none" stroke="#d8262e" stroke-width="2" d="M4 4h12l4 4v12H4zM8 12h8M8 16h8"/></svg></div>
    </div>
    <div class="step" style="left:634px">
      <div class="step-head"><div class="step-num">04</div><div class="step-text">Book your dates and enjoy the trip</div></div>
      <div class="step-icon"><svg width="16" height="16" viewBox="0 0 24 24"><path fill="none" stroke="#d8262e" stroke-width="2.5" d="M5 12l5 5 9-10"/></svg></div>
    </div>
    <div class="done">DONE!</div>
  </section>

  <footer class="site-footer">
    <nav class="foot-nav"><a href="#">Home</a><a href="#">Contact Us</a><a href="#">Testimonials</a><a href="#">Terms</a></nav>
    <div class="follow">Follow Us On<div class="socials"><span></span><span></span><span></span><span></span></div></div>
    <p class="copyright">Copyright © 2017 ClaimVouchly. All Rights Reserved</p>
    <div class="foot-brand"><span class="brand-mark"></span><span class="brand-name">ClaimVouchly</span></div>
  </footer>

</div>
</body>
</html>
```